political campaign lawn sign - Governor's Council in Massachuesetts

We are looking for a political lawn sign. We are running a campaign for Governor's Council in Massachusetts. This sign will be on the lawn of homes and businesses so people driving by will see it. It needs to be simple and bold. The last name is long so maybe it could say vote for Marty and then Kolbeck will be big a bold on the next line??
We need it to say:
Vote for Martin Kolbeck
Governor's Council.

Target Market(s)

local residents

Industry/Entity Type

Politcal Campaign

Font styles to use
Sans Serif
Other font styles liked:
• not sure what font but a modern looking one such as Helvetica, Arial, Sans Seri, sharp sans..

Colors
0054AA
0677BA
7BADD7
CADEEF
E8F1F8
00AB8E
00BBA5
67D7C9
C6EFE9
E9F9F6
FFF300
FFF600
FEFA6F
FFFEC7
FFFEE8

Requirements
Must have
• My name written out with a Capital D and R but lower case for every other letter so its Marty Kolbeck
Nice to have
• modern font , the Colors of the lawn sign should have Blue, Yellow and White something bold that will stand out
Should not have
• any maps of Massachusetts

```html
<!DOCTYPE html>
<html lang="en">
<head>
<meta charset="utf-8">
<title>Marty Kolbeck – Lawn Sign</title>
<link rel="stylesheet" href="https://fonts.googleapis.com/css2?family=Oswald:wght@500;600;700&family=Roboto:wght@400&display=swap">
<style>
  :root {
    --blue-deep: #0054AA;
    --blue-soft: #7BADD7;
    --blue-mist: #CADEEF;
    --white-ice: #E8F1F8;
    --white: #FFFFFF;
    --page: #EDEFF2;
  }
  html, body {
    margin: 0;
    padding: 0;
    width: 720px;
    height: 1200px;
    overflow: hidden;
    background: var(--page);
  }
  .canvas {
    width: 720px;
    height: 1200px;
    display: flex;
    align-items: center;
    justify-content: center;
  }
  .lawn-sign {
    display: block;
    width: 720px;
    height: 480px;
  }
  .sign-headline {
    font-family: "Oswald", sans-serif;
    font-weight: 600;
    fill: var(--white);
  }
  .candidate-first {
    font-family: "Oswald", sans-serif;
    font-weight: 700;
    fill: var(--blue-deep);
  }
  .candidate-last {
    font-family: "Oswald", sans-serif;
    font-weight: 700;
    fill: var(--blue-deep);
  }
  .office-title {
    font-family: "Oswald", sans-serif;
    font-weight: 600;
    fill: var(--white);
  }
  .campaign-site {
    font-family: "Roboto", sans-serif;
    font-weight: 400;
    fill: var(--blue-deep);
  }
</style>
</head>
<body>
<main class="canvas">
  <svg class="lawn-sign" viewBox="0 0 720 480" xmlns="http://www.w3.org/2000/svg" aria-label="Vote for Marty Kolbeck, Governer's Council lawn sign">
    <!-- top field -->
    <rect class="sign-field" x="0" y="0" width="720" height="480" fill="var(--blue-deep)"/>

    <!-- raised hands artwork areas -->
    <rect class="hands-art hands-art--left" x="43" y="30" width="163" height="160" rx="6"
          fill="var(--blue-mist)" opacity="0.85" role="img" aria-label="Illustration of three raised hands"/>
    <rect class="hands-art hands-art--right" x="515" y="30" width="163" height="160" rx="6"
          fill="var(--blue-mist)" opacity="0.85" role="img" aria-label="Illustration of three raised hands"/>

    <!-- roof-shaped name panel with soft edge -->
    <polygon class="roof-edge" points="0,190 360,107 720,190 720,349 0,349" fill="var(--blue-soft)"/>
    <polygon class="name-panel" points="0,197 360,114 720,197 720,349 0,349" fill="var(--white-ice)"/>

    <!-- office band -->
    <rect class="office-band" x="0" y="349" width="720" height="131" fill="var(--blue-soft)"/>
    <rect class="site-rule site-rule--left" x="0" y="448" width="213" height="4" fill="var(--white-ice)"/>
    <rect class="site-rule site-rule--right" x="507" y="448" width="213" height="4" fill="var(--white-ice)"/>

    <!-- text -->
    <text class="sign-headline" x="360" y="89" text-anchor="middle" font-size="68" textLength="214" lengthAdjust="spacingAndGlyphs">VOTE FOR</text>
    <text class="candidate-first" x="360" y="199" text-anchor="middle" font-size="80">Marty</text>
    <text class="candidate-last" x="362" y="335" text-anchor="middle" font-size="172" textLength="572" lengthAdjust="spacingAndGlyphs">Kolbeck</text>
    <text class="office-title" x="361" y="414" text-anchor="middle" font-size="62" textLength="573" lengthAdjust="spacingAndGlyphs">GOVERNER'S COUNCIL</text>
    <text class="campaign-site" x="360" y="462" text-anchor="middle" font-size="36" textLength="270" lengthAdjust="spacingAndGlyphs">voteformarty.net</text>
  </svg>
</main>
</body>
</html>
```